Calm Ridge is a new opened business in takapuna, Auckland, which provide traditional Chinese Therapeutic & relaxation massage. We like to invite more and more people as our customers, especially for the office people near by in the same suburb. We want this flyer to have a pormotion for these kind of people,the probably content of this pormotion is during their lunch break, they will receive a professional Quckily De-stress Relaxation massage for $20 only. We are not the native speaker so we wouldn't use specific sentence to describe. We like the ad be academic and professional.The color we want to use is the same as the file we have attached.also in the flyer we need the direction for the location of our shop.
Industry/Entity Type
Massage
Requirements
Must have
- have a pormotion for office people,the probably content of this pormotion is during their lunch break, they will receive a professional Quckily De-stress Relaxation massage for $20 only.
Nice to have
- our shop address is shop 7, 15 - 29 Pellowan Street, Takapuna, Auckland.
Phone number: 09-5172038
Email: calmridge.nz@brelvio.com
we need the direction for the location of our shop (map)

```html
<!DOCTYPE html>
<html lang="en">
<head>
<meta charset="utf-8">
<title>Calm Ridge – Lunch Break Relaxation Massage Flyer</title>
<link rel="stylesheet" href="https://fonts.googleapis.com/css2?family=Tinos:wght@400;700&family=Libre+Baskerville:wght@700&family=Arimo:wght@400&display=swap">
<style>
  :root {
    --cream: #fdf3c4;
    --butter: #f8e08a;
    --gold: #e6b42c;
    --gold-deep: #d49a17;
    --brown: #5b3a17;
    --brown-dark: #3f2710;
    --orange: #e8622a;
    --ink: #2b1c0c;
    --white: #ffffff;
    --stage: #ece7e0;
  }
  * { box-sizing: border-box; margin: 0; padding: 0; }
  html, body { width: 1200px; height: 766px; overflow: hidden; background: var(--stage); }
  .canvas { position: relative; width: 1200px; height: 766px; }

  .flyer {
    position: absolute; top: 30px; width: 540px; height: 695px; overflow: hidden;
    background: linear-gradient(180deg, var(--cream) 0%, #fbeaa7 55%, var(--butter) 100%);
    box-shadow: 0 4px 10px rgba(0,0,0,.25);
  }
  .flyer--back { left: 30px; }
  .flyer--front { left: 618px; }
  .layer { position: absolute; inset: 0; }

  /* brand */
  .brand { position: absolute; display: flex; align-items: center; gap: 8px; color: var(--brown); }
  .brand__dot { width: 22px; height: 22px; border-radius: 50%; background: var(--orange); flex: none; }
  .brand__text { display: flex; flex-direction: column; }
  .brand__name { font: 700 28px/1 "Tinos", serif; }
  .brand__tag { font: 700 7px/1.2 "Arimo", sans-serif; letter-spacing: .3px; margin-top: 3px; }
  .flyer--back .brand { left: 322px; top: 72px; }
  .flyer--front .brand { left: 292px; top: 74px; }

  /* back: photo + text */
  .photo-top {
    position: absolute; left: 30px; top: 0; width: 265px; height: 190px;
    background: radial-gradient(ellipse at 55% 45%, #e9b995 0%, #f1d2b6 45%, rgba(253,243,196,0) 75%);
  }
  .headline { position: absolute; left: 40px; top: 193px; font: 400 18px/1 "Tinos", serif; color: var(--ink); }
  .copy { position: absolute; font: 400 10px/12.6px "Tinos", serif; color: var(--ink); text-align: justify; }
  .copy--left { left: 40px; top: 222px; width: 237px; }
  .copy--right { left: 293px; top: 192px; width: 218px; }
  .copy strong { font-weight: 700; }
  .copy .contact { white-space: nowrap; }
  .spacer-r { float: right; width: 0; height: 30px; }
  .wrap-r { float: right; clear: right; width: 82px; height: 165px; shape-outside: circle(84px at 80px 80px); }
  .spacer-l { float: left; width: 0; height: 60px; }
  .wrap-l { float: left; clear: left; width: 62px; height: 165px; shape-outside: circle(84px at -18px 82px); }
  .portrait {
    position: absolute; left: 198px; top: 252px; width: 154px; height: 154px; border-radius: 50%;
    border: 7px solid var(--brown);
    background: radial-gradient(circle at 50% 45%, #d9a47e 0%, #b9876a 55%, #e7dccd 100%);
  }
  .address { position: absolute; left: 42px; top: 592px; width: 250px; color: var(--white); font: 400 10px/12px "Arimo", sans-serif; }
  .address__label { margin-bottom: 5px; }
  .web { position: absolute; left: 42px; top: 664px; color: var(--white); font: 400 18px/1 "Arimo", sans-serif; }
  .map {
    position: absolute; left: 317px; top: 538px; width: 184px; height: 135px;
    background: linear-gradient(135deg, #f4f4f4, #dcdcdc); border: 1px solid #c9c9c9;
  }

  /* front: offer */
  .offer { position: absolute; left: 0; top: 560px; width: 540px; height: 135px; color: var(--brown); }
  .offer__lead { position: absolute; left: 240px; top: 6px; font: 700 21px/1 "Libre Baskerville", serif; }
  .offer__ghost { position: absolute; left: 40px; top: 36px; font: 700 40px/1 "Libre Baskerville", serif; color: rgba(91,58,23,.08); white-space: nowrap; }
  .offer__title { position: absolute; left: 50px; top: 32px; font: 700 40px/1 "Libre Baskerville", serif; white-space: nowrap; }
  .offer__price { position: absolute; left: 240px; top: 80px; font: 700 21px/1 "Libre Baskerville", serif; }
  .offer__amount { color: var(--orange); font-size: 27px; }
</style>
</head>
<body>
<main class="canvas">

  <!-- BACK -->
  <section class="flyer flyer--back">
    <div class="photo-top" role="img" aria-label="Photo of a man relaxing face down during a shoulder massage"></div>

    <div class="brand">
      <span class="brand__dot"></span>
      <span class="brand__text">
        <span class="brand__name">Calm Ridge</span>
        <span class="brand__tag">PROFESSIONAL THERAPEUTIC<br>&amp; RELAXATION MASSAGE</span>
      </span>
    </div>

    <h2 class="headline">Your Lunch Break Massage</h2>

    <p class="copy copy--left"><span class="spacer-r"></span><span class="wrap-r"></span>Calm Ridge is a new traditional Chinese therapeutic and relaxation massage clinic in Takapuna, Auckland. Our trained therapists combine time-honoured techniques with a calm, professional setting, helping the body release tension and restore balance. Long hours at a desk can cause stiffness in the neck, shoulders and lower back, as well as fatigue and stress. Regular massage improves circulation, eases muscle tightness and supports clearer thinking for the rest of the working day. Each treatment is adapted to your needs, whether you seek gentle relaxation or focused therapeutic work on problem areas. We welcome every visitor with clean rooms and soothing surroundings, so even a short visit feels like a true break.</p>

    <p class="copy copy--right"><span class="spacer-l"></span><span class="wrap-l"></span><strong>Lunch break offer for office people.</strong> Working in Takapuna? Make the most of your lunch hour. Walk in during your lunch break and receive a professional Quick De-stress Relaxation Massage for only $20. This focused session targets the neck, shoulders and back, where office work leaves the most tension, so you return to your desk refreshed and ready for the afternoon. We keep lunchtime appointments on schedule, so you are back at work on time. Bookings are recommended and walk-ins are welcome. To reserve your time, please call <span class="contact">09-5172038</span> or email <span class="contact">calmridge.nz@brelvio.com</span>. Our shop is a short walk from the town centre; see the map below for directions.</p>

    <div class="portrait" role="img" aria-label="Circular photo of a man receiving a calming face massage"></div>

    <svg class="layer" width="540" height="695" viewBox="0 0 540 695" aria-hidden="true">
      <path d="M0 548 C140 520 330 540 540 478 L540 505 C360 548 170 538 0 575 Z" fill="var(--gold)"/>
      <path d="M0 562 C160 530 340 556 540 496 L540 695 L0 695 Z" fill="var(--brown)"/>
      <path d="M40 548 C200 525 360 538 540 486" fill="none" stroke="var(--white)" stroke-width="1.5" opacity=".7"/>
    </svg>

    <div class="address">
      <p class="address__label">ADDRESS</p>
      <p>shop 7, 15 - 29 Pellowan Street, Takapuna, Auckland</p>
      <p>Phone: 09-5172038</p>
      <p>Email: calmridge.nz@brelvio.com</p>
    </div>
    <p class="web">www.calmridgemassage.nz</p>
    <div class="map" role="img" aria-label="Street map showing directions to the shop"></div>
  </section>

  <!-- FRONT -->
  <section class="flyer flyer--front">
    <svg class="layer" width="540" height="695" viewBox="0 0 540 695" role="img" aria-label="Photo of a couple receiving relaxation massages beside candles">
      <defs>
        <linearGradient id="spaPhoto" x1="0" y1="0" x2="1" y2="1">
          <stop offset="0" stop-color="#f3e6d6"/>
          <stop offset=".45" stop-color="#e3b28c"/>
          <stop offset="1" stop-color="#f6efe4"/>
        </linearGradient>
        <radialGradient id="handsPhoto" cx=".5" cy=".5" r=".6">
          <stop offset="0" stop-color="#e5b091"/>
          <stop offset="1" stop-color="#c98e6c"/>
        </radialGradient>
        <path id="arcText" d="M40 140 A80 80 0 0 1 200 110"/>
      </defs>
      <path d="M0 170 C140 245 330 250 540 205 L540 500 C380 500 190 510 0 555 Z" fill="url(#spaPhoto)"/>
      <path d="M110 200 C250 250 400 240 540 210 L540 222 C390 256 250 262 110 212 Z" fill="var(--orange)"/>
      <path d="M0 560 C200 505 380 500 540 490 L540 505 C380 510 200 522 0 575 Z" fill="var(--white)"/>
      <path d="M0 575 C200 522 380 510 540 505 L540 520 C380 524 200 536 0 590 Z" fill="var(--gold)" opacity=".6"/>
      <circle cx="114" cy="168" r="64" fill="url(#handsPhoto)" stroke="var(--orange)" stroke-width="7"/>
      <text font-family="Tinos, serif" font-size="16" fill="var(--brown)" letter-spacing="1"><textPath href="#arcText">RELAXATION MASSAGE</textPath></text>
    </svg>

    <div class="brand">
      <span class="brand__dot"></span>
      <span class="brand__text">
        <span class="brand__name">Calm Ridge</span>
        <span class="brand__tag">PROFESSIONAL THERAPEUTIC<br>&amp; RELAXATION MASSAGE</span>
      </span>
    </div>

    <div class="offer">
      <p class="offer__ghost" aria-hidden="true">Relaxation massage</p>
      <p class="offer__lead">Quckily De-stress</p>
      <h1 class="offer__title">Relaxation massage</h1>
      <p class="offer__price">for <span class="offer__amount">$20</span> only.</p>
    </div>
  </section>

</main>
</body>
</html>
```